Ad Banner for Insight Net Panel

This banner is used in "Query Harbor" web site. This web site provides a single place for all employees to ask questions related to work. There will be dedicated subject matter experts to respond to all questions. The web site also provides "Talent Atlas" where employee can see the list of all experts in the company.
1. Banner size: 940x380
2. Business background: Provides maintenance, design and engineering, construction, machinery operation, material procurement and production management services for petrochemical and refinery business
3. We would like to see designs that
- Promote the ask questions in "Query Harbor" system
- Promote that company has experts in the areas of "Maintenance and Engineering" and can be found in "Talent Atlas"
- Encourage employees to advocate himself to be an expert by sending an email to a specific email address.
- Do not include picture of real people in the banner

```html
<!DOCTYPE html>
<html lang="en">
<head>
<meta charset="utf-8">
<title>Query Harbor – Banner</title>
<link rel="stylesheet" href="https://fonts.googleapis.com/css2?family=Varela+Round&display=swap">
<style>
  :root {
    --yellow: #f3c12f;
    --slate: #8b9ca8;
    --ring: #f0f0f0;
    --ring-edge: #e4e4e4;
    --white: #ffffff;
  }
  * { margin: 0; padding: 0; box-sizing: border-box; }
  html, body { width: 1200px; height: 457px; overflow: hidden; background: var(--white); }
  .banner {
    position: relative;
    width: 1200px;
    height: 457px;
    font-family: "Varela Round", "Helvetica Neue", Arial, sans-serif;
    color: var(--slate);
  }
  .badge { position: absolute; display: block; }
  .badge--question { left: 21px; top: 48px; }
  .badge--mail { left: 494px; top: 217px; }
  .badge--search { left: 853px; top: 42px; }

  .brand {
    position: absolute;
    left: 0; right: 0; top: 4px;
    text-align: center;
    font-size: 64px;
    letter-spacing: 1px;
    color: var(--slate);
    line-height: 1;
  }
  .tagline {
    position: absolute;
    left: 0; right: 0; top: 84px;
    text-align: center;
    font-size: 25px;
    line-height: 36px;
  }
  .label {
    position: absolute;
    text-align: center;
    line-height: 1.3;
  }
  .label--questions { left: 0; width: 302px; top: 332px; font-size: 35px; line-height: 54px; }
  .label--expert { left: 400px; width: 342px; top: 386px; font-size: 35px; color: var(--yellow); }
  .label--directory { left: 782px; width: 418px; top: 330px; }
  .label--directory .title { display: block; font-size: 35px; line-height: 46px; }
  .label--directory .sub { display: block; font-size: 23px; line-height: 32px; }
  .label--directory .area { display: block; font-size: 26px; line-height: 34px; }
</style>
</head>
<body>
<main class="banner">
  <svg class="badge badge--question" width="262" height="262" viewBox="0 0 262 262" aria-hidden="true">
    <circle cx="131" cy="131" r="128" fill="var(--ring)" stroke="var(--ring-edge)" stroke-width="2"/>
    <circle cx="131" cy="131" r="98" fill="var(--yellow)"/>
    <path d="M104 108 a27 27 0 1 1 40 24 c-9 5 -13 9 -13 19 v6" fill="none" stroke="var(--white)" stroke-width="18" stroke-linecap="round"/>
    <rect x="121" y="170" width="20" height="20" rx="4" fill="var(--white)"/>
  </svg>

  <h1 class="brand">QUERY HARBOR</h1>
  <p class="tagline">a single place for all employees<br>to ask questions related to work</p>

  <svg class="badge badge--mail" width="154" height="154" viewBox="0 0 154 154" aria-hidden="true">
    <circle cx="77" cy="77" r="75" fill="var(--ring)" stroke="var(--ring-edge)" stroke-width="2"/>
    <circle cx="77" cy="77" r="62" fill="var(--white)"/>
    <rect x="27" y="46" width="100" height="64" fill="var(--yellow)"/>
    <path d="M27 46 L77 84 L127 46" fill="none" stroke="var(--white)" stroke-width="3"/>
  </svg>

  <svg class="badge badge--search" width="262" height="262" viewBox="0 0 262 262" aria-hidden="true">
    <circle cx="131" cy="131" r="128" fill="var(--ring)" stroke="var(--ring-edge)" stroke-width="2"/>
    <circle cx="131" cy="131" r="108" fill="var(--white)"/>
    <circle cx="128" cy="118" r="64" fill="none" stroke="var(--yellow)" stroke-width="14"/>
    <line x1="168" y1="170" x2="196" y2="208" stroke="var(--yellow)" stroke-width="16" stroke-linecap="round"/>
  </svg>

  <p class="label label--questions">Questions<br>related to work</p>
  <p class="label label--expert">be an expert</p>
  <p class="label label--directory">
    <span class="title">Talent Atlas</span>
    <span class="sub">EXPERTS IN</span>
    <span class="area">Maintenance and Engineering</span>
  </p>
</main>
</body>
</html>
```